New grafic design homepage www.klimvaro.be
Needs
The homepage design should improve and build on the design of www.dovamex.nl and www.wuntra.be. Following requirements:
1. Functional and visually oriented
2. Icons for "drogen", "verwarming" (5) etc on the website www.klimvaro.be must be used, size could be varied (see attachments for example)
3. Call to action for webshop
4. Call to action for online chat, call me, email me and contact form
5. Online brochure button, search per product section, search for usage
section.
6. Creative design for project references/testimonials section
7. Use www.dovamex as a base for the design..I like this design but would
like to see improvements.
8. Less is more, so please work on an intuitive and functional design
using images.
9. Visible "Why Klimvaro" section with bulletpoint presentation of USP's
10. LOGO text changed to "Shape your comfort"
Company description
Rental business. Company rents out equipment for air quality control such as air conditioners, coolers, heaters, humidifyers, dryers to Belgium customers.
Target group
Target market segments are: construction companies, industry with climate control issues. Owners of shops, server rooms, organizers of events, office buildings. Construction site operators.
Colors, favourites and other requirements
Improve the design of the homepages of www.dovamex.nl and www.wuntra.be using creative ideas to incorporate the requirements.
Use the 5 icons for the 5 product ranges (see attachments)

```html
<!DOCTYPE html>
<html lang="nl">
<head>
<meta charset="utf-8">
<title>Klimvaro – Verhuur luchtbehandeling</title>
<link href="https://fonts.googleapis.com/css2?family=Open+Sans:wght@300;400;600;700&display=swap" rel="stylesheet">
<style>
:root{
  --orange:#f39200;
  --orange-dark:#e07f00;
  --ink:#3c3c3c;
  --muted:#8a8a8a;
  --line:#e3e3e3;
  --sky-top:#2f7fcf;
  --sky-bottom:#d7e8f6;
  --footer:#3b3b3b;
  --footer-text:#bdbdbd;
  --bottom-bar:#2c2c2c;
  --page:#ffffff;
}
*{box-sizing:border-box;margin:0;padding:0}
html,body{width:1200px;height:768px;overflow:hidden}
body{font-family:"Open Sans",Arial,sans-serif;color:var(--ink);background:var(--page);position:relative}

.site-header{height:60px;border-bottom:1px solid var(--line);display:flex;align-items:center;padding:0 216px;justify-content:space-between}
.brand{display:flex;align-items:center;gap:8px;font-weight:700;font-size:20px;color:var(--ink);letter-spacing:.5px}
.brand-dot{width:14px;height:14px;border-radius:50%;background:var(--orange)}
.main-nav{display:flex;gap:0;height:100%}
.main-nav a{display:flex;align-items:center;padding:0 14px;font-size:11px;color:var(--muted);text-decoration:none;height:100%;border-bottom:3px solid transparent}
.main-nav a.is-active{color:var(--orange);border-bottom-color:var(--orange);font-weight:600}

.hero{position:relative;height:290px;background:linear-gradient(180deg,var(--sky-top) 0%,#6aa9e3 45%,var(--sky-bottom) 100%)}
.hero-tagline{position:absolute;left:216px;top:36px;display:flex;align-items:center;gap:8px;color:#fff}
.hero-tagline .mark{width:22px;height:22px;border-radius:50%;background:#fff}
.hero-tagline strong{display:block;font-size:13px;font-weight:700}
.hero-tagline span{display:block;font-size:10px;font-weight:300}
.hero-visual{position:absolute;left:440px;top:20px;width:330px;height:210px;border-radius:50% 50% 8px 8px;background:radial-gradient(circle at 50% 45%,#f6d22b 0%,#e9b90f 45%,#7a8a96 75%,rgba(122,138,150,0) 100%)}
.hero-welcome{position:absolute;right:216px;top:46px;text-align:right}
.hero-welcome h1{background:var(--orange);color:#fff;font-size:22px;font-weight:600;padding:6px 14px;display:inline-block}
.hero-welcome p{background:#fff;color:var(--orange);font-size:13px;padding:4px 14px;display:inline-block;margin-top:2px}

.product-ranges{position:absolute;left:216px;top:230px;width:768px;display:flex;gap:6px;justify-content:center}
.range-card{width:148px;background:#fff;box-shadow:0 2px 8px rgba(0,0,0,.18)}
.range-card .thumb{height:118px;margin:10px 20px 6px;border-radius:4px}
.thumb.cooling{background:linear-gradient(180deg,#eef1f3,#b9c2c9)}
.thumb.heating{background:linear-gradient(180deg,#5ab0ea,#1f74c2)}
.thumb.ventilation{background:radial-gradient(circle,#f7d531 30%,#e2b20c 70%,#fff 72%)}
.thumb.drying{background:linear-gradient(180deg,#f6d53a,#d9a80c)}
.thumb.humidifying{background:linear-gradient(180deg,#e6e9eb,#a8b0b6)}
.range-card .label{border-top:3px solid var(--orange);padding:7px 0;text-align:center;font-size:11px;color:var(--muted)}
.range-card .label b{color:var(--ink);font-weight:700}

.content{position:absolute;left:216px;top:410px;width:768px;display:flex;gap:60px}
.content h2{font-size:17px;font-weight:400;padding-bottom:6px;border-bottom:2px solid var(--orange);margin-bottom:10px}
.content h2 b{font-weight:700}
.why{flex:1}
.usp-list{list-style:none}
.usp-list li{display:flex;align-items:center;gap:8px;font-size:11px;color:#666;line-height:22px}
.usp-list svg{flex:none}
.testimonials{flex:1}
.quote{margin-bottom:10px}
.quote strong{font-size:11px;display:block}
.quote p{font-size:10.5px;color:var(--muted);line-height:15px}

.site-footer{position:absolute;left:0;top:600px;width:1200px;height:142px;background:var(--footer);padding:22px 216px;display:flex;gap:40px;color:var(--footer-text)}
.site-footer h3{color:#fff;font-size:13px;font-weight:700;margin-bottom:6px}
.footer-col{font-size:10.5px;line-height:18px}
.footer-col.about{width:170px}
.footer-col.links{width:130px}
.contact-list{margin-left:auto;list-style:none}
.contact-list li{display:flex;gap:8px;margin-bottom:8px;font-size:10.5px;line-height:14px}
.contact-list b{color:#fff;display:block}
.bottom-bar{position:absolute;left:0;top:742px;width:1200px;height:26px;background:var(--bottom-bar);color:#888;font-size:9.5px;padding:6px 216px}
</style>
</head>
<body>
<header class="site-header">
  <div class="brand"><span class="brand-dot"></span>KLIMVARO</div>
  <nav class="main-nav">
    <a class="is-active" href="#">Home</a>
    <a href="#">Productoverzicht</a>
    <a href="#">Toepassingen</a>
    <a href="#">Webshop</a>
    <a href="#">Nieuws</a>
    <a href="#">Contact</a>
  </nav>
</header>

<section class="hero">
  <div class="hero-tagline"><span class="mark"></span><div><strong>Klimvaro</strong><span>Shape your comfort</span></div></div>
  <div class="hero-visual" role="img" aria-label="Gele ventilatoren en luchtbehandelingstoestellen"></div>
  <div class="hero-welcome">
    <h1>Welkom bij KLIMVARO</h1><br>
    <p>Verhuur Luchtbehandeling</p>
  </div>
</section>

<div class="product-ranges">
  <div class="range-card"><div class="thumb cooling" role="img" aria-label="Koeltoestel"></div><div class="label"><b>Koeling</b> Verhuur</div></div>
  <div class="range-card"><div class="thumb heating" role="img" aria-label="Verwarmingstoestel"></div><div class="label"><b>Verwarming</b> Verhuur</div></div>
  <div class="range-card"><div class="thumb ventilation" role="img" aria-label="Ventilator"></div><div class="label"><b>Ventilatie</b> Verhuur</div></div>
  <div class="range-card"><div class="thumb drying" role="img" aria-label="Bouwdroger"></div><div class="label"><b>Drogen</b> Verhuur</div></div>
  <div class="range-card"><div class="thumb humidifying" role="img" aria-label="Luchtbevochtiger"></div><div class="label"><b>Bevochtiging</b> Verhuur</div></div>
</div>

<main class="content">
  <section class="why">
    <h2>Waarom <b>KLIMVARO</b></h2>
    <ul class="usp-list">
      <li><svg width="10" height="10" viewBox="0 0 10 10"><path d="M1 5l3 3 5-6" stroke="#f39200" stroke-width="2" fill="none"/></svg>Snelle levering in heel België</li>
      <li><svg width="10" height="10" viewBox="0 0 10 10"><path d="M1 5l3 3 5-6" stroke="#f39200" stroke-width="2" fill="none"/></svg>Ruim en modern verhuurpark</li>
      <li><svg width="10" height="10" viewBox="0 0 10 10"><path d="M1 5l3 3 5-6" stroke="#f39200" stroke-width="2" fill="none"/></svg>Deskundig advies op maat</li>
      <li><svg width="10" height="10" viewBox="0 0 10 10"><path d="M1 5l3 3 5-6" stroke="#f39200" stroke-width="2" fill="none"/></svg>Service 24 uur per dag</li>
      <li><svg width="10" height="10" viewBox="0 0 10 10"><path d="M1 5l3 3 5-6" stroke="#f39200" stroke-width="2" fill="none"/></svg>Scherpe tarieven voor korte en lange huur</li>
    </ul>
  </section>
  <section class="testimonials">
    <h2>Wat <b>klanten</b> zeggen</h2>
    <div class="quote"><strong>Lieven Dartois</strong><p>Snelle levering en een vlotte service op de werf.</p></div>
    <div class="quote"><strong>Sofie Verlinde</strong><p>Goed advies, het toestel deed perfect zijn werk.</p></div>
    <div class="quote"><strong>Bouwgroep Hestra</strong><p>Al jaren een betrouwbare partner voor onze projecten.</p></div>
  </section>
</main>

<footer class="site-footer">
  <div class="footer-col about"><h3>KLIMVARO</h3>Verhuur van klimaattoestellen<br>voor bouw, industrie en events</div>
  <div class="footer-col links"><br>Productoverzicht<br>Toepassingen<br>Webshop</div>
  <div class="footer-col links"><br>Nieuws<br>Referenties<br>Brochure downloaden</div>
  <ul class="contact-list">
    <li><svg width="12" height="14" viewBox="0 0 12 14"><path d="M6 13S1 8 1 5a5 5 0 0110 0c0 3-5 8-5 8z" fill="#f39200"/><circle cx="6" cy="5" r="2" fill="#3b3b3b"/></svg><span><b>Adres</b>Veldstraat 14, 9000 Gent</span></li>
    <li><svg width="12" height="14" viewBox="0 0 12 14"><path d="M2 1h3l1 3-2 1a7 7 0 003 4l1-2 3 1v3c0 1-1 2-2 2C5 13 0 8 0 3c0-1 1-2 2-2z" fill="#f39200"/></svg><span><b>Telefoon</b>09 000 12 34</span></li>
    <li><svg width="12" height="14" viewBox="0 0 12 14"><rect x="0" y="3" width="12" height="8" fill="#f39200"/><path d="M0 3l6 5 6-5" stroke="#3b3b3b" fill="none"/></svg><span><b>Email</b>info@klimvaro.be</span></li>
  </ul>
</footer>
<div class="bottom-bar">© Klimvaro – www.klimvaro.be</div>
</body>
</html>
```